QuadLantern--Help Us look fresh and new to companies, college students and college career centers!

We just designed a new logo and would like to freshen-up and make our business cards a bit more modern. Not crazy-modern like Velmont, but modern like metro-style and fresh like fruit. We use three logos with a combination of two colors each, and three colors total. We are looking for a single format to apply to three different cards/color schemes (green/blue to give out to companies, orange/green for students, and orange/blue for university career centers). Thanks everyone--looking forward to seeing your designs!!

Target Market(s)

Three styles: companies, college students/grads, college career centers

Industry/Entity Type

College

Contact Information for Business Card

Address: 5718 Harlow Street, Suite 412, Seattle, WA 98109. Need a spot for email address, web address (www.quadlantern.example), and phone numbers (main, direct, mobile). Don't open that website unless you want to lose your lunch--it is waaaay old and outdated. See this link instead, http://preview.mossgrovedev.example/QuadLantern/HiringTools, for our new website design in progress.

Font styles to use
Sans Serif

Requirements
Must have
• Please use the logos supplied. Would like text to be grey but printable, like a "light" type style that is metro-type with sans-serif. NOT black text. Modern. For inspiration, here's a link to our work-in-progress website we are planning to launch soon: http://preview.mossgrovedev.example/QuadLantern/HiringTools
Nice to have
• Would like to see something unique and different in a "metro" style. Clean and not cluttered.
Should not have
• No odd-sized cards

```html
<!DOCTYPE html>
<html lang="en">
<head>
<meta charset="utf-8">
<title>QuadLantern Business Card</title>
<link href="https://fonts.googleapis.com/css2?family=Exo+2:wght@300;400;600;700&display=swap" rel="stylesheet">
<style>
  :root {
    --backdrop: #e9e7e3;
    --card-blue: #1a7cc4;
    --card-green: #7cc242;
    --card-white: #f4f5f6;
    --card-shade: #e3e5e7;
    --text-light: #ffffff;
    --brand-blue: #1a7cc4;
  }
  html, body {
    margin: 0;
    width: 1200px;
    height: 900px;
    overflow: hidden;
    background: var(--backdrop);
  }
  .business-card {
    position: absolute;
    left: 100px;
    top: 164px;
    width: 1000px;
    height: 572px;
    background: linear-gradient(120deg, var(--card-white) 55%, var(--card-shade));
    box-shadow: 0 10px 30px rgba(0,0,0,0.18);
    overflow: hidden;
    font-family: "Exo 2", sans-serif;
  }
  .card-shapes {
    position: absolute;
    inset: 0;
  }
  .contact-panel {
    position: absolute;
    left: 62px;
    top: 58px;
    color: var(--text-light);
  }
  .person-name {
    margin: 0;
    font-size: 34px;
    font-weight: 400;
    letter-spacing: 2px;
    white-space: nowrap;
  }
  .person-title {
    margin: 2px 0 0;
    font-size: 21px;
    font-weight: 300;
    letter-spacing: 0.5px;
  }
  .address {
    margin: 34px 0 0;
    font-size: 21px;
    font-weight: 300;
    line-height: 1.35;
    font-style: normal;
    letter-spacing: 0.5px;
  }
  .contact-list {
    list-style: none;
    padding: 0;
    margin: 32px 0 0;
  }
  .contact-list li {
    display: flex;
    align-items: center;
    gap: 14px;
    font-size: 19px;
    font-weight: 300;
    letter-spacing: 1px;
    height: 38px;
    white-space: nowrap;
  }
  .contact-icon {
    width: 20px;
    height: 20px;
    flex: none;
  }
  .brand-lockup {
    position: absolute;
    left: 575px;
    top: 240px;
    display: flex;
    align-items: center;
    gap: 12px;
    white-space: nowrap;
  }
  .brand-dot {
    width: 26px;
    height: 26px;
    border-radius: 50%;
    background: var(--card-green);
    flex: none;
  }
  .brand-name {
    font-size: 50px;
    font-weight: 700;
    color: var(--brand-blue);
    letter-spacing: -0.5px;
  }
</style>
</head>
<body>
  <div class="business-card">
    <svg class="card-shapes" viewBox="0 0 1000 572" width="1000" height="572" aria-hidden="true">
      <path d="M0 0 H600 Q420 150 420 572 H0 Z" fill="var(--card-blue)"/>
      <path d="M640 18 Q470 150 452 420 Q480 170 660 24 Z" fill="var(--card-green)"/>
    </svg>

    <section class="contact-panel">
      <h1 class="person-name">MARCUS HALLORAN</h1>
      <p class="person-title">Managing Director</p>
      <address class="address">5718 Harlow Street, Suite 412<br>Seattle, WA 98109</address>
      <ul class="contact-list">
        <li>
          <svg class="contact-icon" viewBox="0 0 20 20"><path d="M5 2 L8 6 L6.5 8 Q8 12 12 13.5 L14 12 L18 15 L16 18 Q9 18 5 13 Q2 8 3 4 Z" fill="#fff"/></svg>
          206 555 0142
        </li>
        <li>
          <svg class="contact-icon" viewBox="0 0 20 20"><rect x="5" y="1.5" width="10" height="17" rx="2" fill="none" stroke="#fff" stroke-width="1.6"/><circle cx="10" cy="15.5" r="1" fill="#fff"/></svg>
          206 555 0178
        </li>
        <li>
          <svg class="contact-icon" viewBox="0 0 20 20"><rect x="3" y="2" width="14" height="17" fill="none" stroke="#fff" stroke-width="1.6"/><path d="M6 6h2M12 6h2M6 10h2M12 10h2M6 14h2M12 14h2" stroke="#fff" stroke-width="1.6"/></svg>
          206 555 0193
        </li>
        <li>
          <svg class="contact-icon" viewBox="0 0 20 20"><rect x="1.5" y="4" width="17" height="12" fill="#fff"/><path d="M1.5 4 L10 11 L18.5 4" fill="none" stroke="var(--card-blue)" stroke-width="1.4"/></svg>
          hello@quadlantern.example
        </li>
        <li>
          <svg class="contact-icon" viewBox="0 0 20 20"><circle cx="10" cy="10" r="8" fill="none" stroke="#fff" stroke-width="1.5"/><ellipse cx="10" cy="10" rx="3.5" ry="8" fill="none" stroke="#fff" stroke-width="1.3"/><path d="M2 10h16M3.5 6h13M3.5 14h13" stroke="#fff" stroke-width="1.2"/></svg>
          www.quadlantern.example
        </li>
      </ul>
    </section>

    <div class="brand-lockup">
      <span class="brand-dot"></span>
      <span class="brand-name">QuadLantern</span>
    </div>
  </div>
</body>
</html>
```